" disponibiliza material de professores renomados para download, realiza uma avaliação da compreensão do conteúdo e emite um certificado se for aprovado "

```html
<!DOCTYPE html>
<html lang="pt-BR">
<head>
<meta charset="utf-8">
<title>Lumina Cursos Online — Papelaria</title>
<link href="https://fonts.googleapis.com/css2?family=Lato:wght@300;400&display=swap" rel="stylesheet">
<style>
  :root {
    --backdrop: #2b2b2d;
    --paper: #ffffff;
    --folder: #2f3033;
    --folder-edge: #26272a;
    --teal: #4fa3b0;
    --rule-grey: #c9cdd0;
    --ink-grey: #6b7074;
    --folder-ink: #a7acb0;
  }
  * { margin: 0; padding: 0; box-sizing: border-box; }
  html, body { width: 1200px; height: 1200px; overflow: hidden; }
  body { background: var(--backdrop); font-family: "Lato", sans-serif; position: relative; }

  .brand {
    display: inline-flex; align-items: center;
    font-family: "Lato", sans-serif; font-weight: 300; color: var(--teal);
    white-space: nowrap;
  }
  .brand__dot { border: 1px solid var(--teal); border-radius: 50%; flex: none; }

  /* Letterhead */
  .letterhead {
    position: absolute; left: 461px; top: 67px; width: 343px; height: 461px;
    background: var(--paper);
  }
  .letterhead__brand { position: absolute; top: 24px; left: 0; right: 0; text-align: center; }
  .letterhead__brand .brand { font-size: 10px; gap: 5px; }
  .letterhead__brand .brand__dot { width: 9px; height: 9px; }
  .letterhead__rule-top {
    position: absolute; left: 22px; right: 22px; top: 48px; height: 1px; background: var(--rule-grey);
  }
  .letterhead__watermark { position: absolute; left: 66px; top: 95px; width: 211px; height: 211px; }
  .letterhead__rule-bottom {
    position: absolute; left: 22px; right: 22px; top: 432px; height: 1px; background: var(--rule-grey);
  }
  .letterhead__contacts {
    position: absolute; left: 22px; right: 22px; top: 440px;
    display: flex; justify-content: space-between;
  }
  .contact-item { display: flex; gap: 4px; align-items: flex-start; }
  .contact-item__dot { width: 5px; height: 5px; background: var(--teal); margin-top: 1px; flex: none; }
  .contact-item__text { font-size: 4.5px; line-height: 6px; color: var(--ink-grey); }

  /* Folders */
  .folder {
    position: absolute; top: 583px; width: 350px; height: 485px;
    background: var(--folder); border: 1px solid var(--folder-edge);
  }
  .folder--back { left: 215px; }
  .folder--front { left: 605px; }
  .folder__rule {
    position: absolute; left: 0; right: 0; top: 466px; height: 2px; background: var(--teal);
  }
  .folder--back .folder__watermark { position: absolute; left: 95px; top: 75px; width: 160px; height: 160px; }
  .folder__footer {
    position: absolute; left: 14px; right: 16px; top: 412px;
    display: flex; justify-content: space-between; align-items: flex-end;
  }
  .folder__contacts { border-left: 2px solid var(--teal); padding-left: 6px; }
  .folder__contacts p { font-size: 5px; line-height: 8px; color: var(--folder-ink); }
  .folder__footer .brand { font-size: 10px; gap: 5px; }
  .folder__footer .brand__dot { width: 9px; height: 9px; }

  .cover-brand { position: absolute; left: 0; right: 0; top: 214px; text-align: center; }
  .cover-brand .brand { font-size: 26px; gap: 12px; }
  .cover-brand .brand__dot { width: 22px; height: 22px; border-width: 2px; }
</style>
</head>
<body>

  <section class="letterhead">
    <div class="letterhead__brand">
      <span class="brand"><span class="brand__dot"></span>Lumina Cursos Online</span>
    </div>
    <div class="letterhead__rule-top"></div>
    <svg class="letterhead__watermark" viewBox="0 0 211 211" role="img" aria-label="Faint background decoration area">
      <defs>
        <radialGradient id="lh-fade" cx="50%" cy="50%" r="50%">
          <stop offset="0%" stop-color="#e6f1f3"/>
          <stop offset="100%" stop-color="#ffffff"/>
        </radialGradient>
      </defs>
      <circle cx="105.5" cy="105.5" r="104" fill="url(#lh-fade)" stroke="#eef2f3" stroke-width="1"/>
    </svg>
    <div class="letterhead__rule-bottom"></div>
    <div class="letterhead__contacts">
      <div class="contact-item">
        <span class="contact-item__dot"></span>
        <p class="contact-item__text">(11) 4000-2020<br>(11) 98000-1234</p>
      </div>
      <div class="contact-item">
        <span class="contact-item__dot"></span>
        <p class="contact-item__text">contato@luminacursos.com.br</p>
      </div>
      <div class="contact-item">
        <span class="contact-item__dot"></span>
        <p class="contact-item__text">Rua das Acácias, 120<br>São Paulo - SP</p>
      </div>
    </div>
  </section>

  <section class="folder folder--back">
    <svg class="folder__watermark" viewBox="0 0 160 160" role="img" aria-label="Faint background decoration area">
      <defs>
        <radialGradient id="fb-fade" cx="50%" cy="50%" r="50%">
          <stop offset="0%" stop-color="#3a3c40"/>
          <stop offset="100%" stop-color="#2f3033"/>
        </radialGradient>
      </defs>
      <circle cx="80" cy="80" r="78" fill="url(#fb-fade)"/>
    </svg>
    <div class="folder__footer">
      <div class="folder__contacts">
        <p>luminacursos.com.br</p>
        <p>Rua das Acácias, 120</p>
        <p>São Paulo - SP · (11) 4000-2020</p>
        <p>contato@luminacursos.com.br</p>
      </div>
      <span class="brand"><span class="brand__dot"></span>Lumina Cursos Online</span>
    </div>
    <div class="folder__rule"></div>
  </section>

  <section class="folder folder--front">
    <div class="cover-brand">
      <span class="brand"><span class="brand__dot"></span>Lumina Cursos Online</span>
    </div>
    <div class="folder__rule"></div>
  </section>

</body>
</html>
```